Attorney Business Card

I need a business card that looks professional yet modern. I am an Attorney. , I need a professional yet modern business card for my law practice. My logo and information have been uploaded. , I need a business card that looks professional yet modern. I am an Attorney. , I need a professional yet modern business card for my law practice. My logo and information have been uploaded.

Industry/Entity Type

Business

Requirements
Must have
• My logo which has been uploaded , my logo , My logo which has been uploaded , my logo

```html
<!DOCTYPE html>
<html lang="en">
<head>
<meta charset="utf-8">
<title>Halvern Law Firm – Business Card</title>
<link rel="stylesheet" href="https://fonts.googleapis.com/css2?family=Archivo:wght@400;600;700&display=swap">
<style>
  :root {
    --backdrop: #6e7174;
    --card-front: #eef0f2;
    --card-back: #262626;
    --ink: #1f2326;
    --navy: #1f4f86;
    --rule: #2f5f95;
    --back-mark: #1b1b1b;
    --back-text: #e8e8e8;
  }
  * { box-sizing: border-box; margin: 0; padding: 0; }
  html, body { width: 1200px; height: 900px; overflow: hidden; }
  body {
    background: var(--backdrop);
    font-family: "Archivo", Arial, sans-serif;
    display: flex;
    align-items: center;
    justify-content: center;
    gap: 90px;
  }
  .card {
    width: 320px;
    height: 560px;
    position: relative;
    box-shadow: 0 18px 40px rgba(0,0,0,0.25);
  }
  .card--front {
    background: var(--card-front);
    color: var(--ink);
    padding: 40px 40px 0;
  }
  .firm-name {
    height: 150px;
    display: flex;
    align-items: center;
    justify-content: center;
    font-family: "Archivo", Arial, sans-serif;
    font-weight: 600;
    font-size: 20px;
    letter-spacing: 2px;
    text-transform: uppercase;
    color: var(--navy);
  }
  .rule { border: 0; border-top: 1.5px solid var(--rule); }
  .card--front .rule { margin: 12px 0; }
  .firm-name + .rule { margin-top: 14px; }
  .holder__name { font-weight: 700; font-size: 17px; letter-spacing: -0.2px; }
  .holder__title { color: var(--navy); font-size: 13.5px; margin-top: 3px; }
  .contact { list-style: none; font-size: 13.5px; line-height: 1.3; }
  .contact__key { color: var(--navy); font-weight: 600; display: inline-block; width: 16px; }
  .contact__email { padding-left: 16px; }
  .address { font-size: 13px; line-height: 1.35; font-style: normal; padding-left: 16px; }

  .card--back { background: var(--card-back); }
  .back-mark {
    position: absolute;
    top: 40px; left: 0; right: 0;
    height: 150px;
    display: flex;
    align-items: center;
    justify-content: center;
    font-family: "Archivo", Arial, sans-serif;
    font-weight: 600;
    font-size: 20px;
    letter-spacing: 2px;
    text-transform: uppercase;
    color: var(--back-mark);
  }
  .back-footer {
    position: absolute;
    left: 110px; right: 40px; bottom: 150px;
  }
  .back-footer .rule { border-top-width: 1px; margin-bottom: 14px; }
  .web { color: var(--back-text); font-size: 12.5px; letter-spacing: 2px; text-align: center; }
</style>
</head>
<body>
  <article class="card card--front">
    <h1 class="firm-name">Halvern Law Firm</h1>
    <hr class="rule">
    <div class="holder">
      <p class="holder__name">Jordan Halvern, ESQ.</p>
      <p class="holder__title">Attorney at law</p>
    </div>
    <hr class="rule">
    <ul class="contact">
      <li><span class="contact__key">T</span>310.555.0142</li>
      <li><span class="contact__key">F</span>310.555.0187</li>
      <li><span class="contact__key">M</span>310.555.0163</li>
      <li class="contact__email">jordan@hlvfirm.com</li>
    </ul>
    <hr class="rule">
    <address class="address">
      1820 Canyon Crest Blvd.<br>
      Penthouse<br>
      Westbrook, CA 90410
    </address>
  </article>

  <article class="card card--back">
    <p class="back-mark">Halvern Law Firm</p>
    <div class="back-footer">
      <hr class="rule">
      <p class="web">www.hlvfirm.com</p>
    </div>
  </article>
</body>
</html>
```